Accounting and Tax Professional

New business with a business model based on good service and bright staff,

Jordan Pike B.Com CPA DIRECTOR

"Kestrel Ledger Services Pty Ltd"
ABN 47 382 615 908

Registered Tax Agent
PROFESSIONAL PERSONABLE TIMELY OR "PROFESSIONAL ADVICE TAILORED TO SUIT YOU"
Superannuation|Business services|Management consulting|Taxation|Software support
E Jordan@KestrelLedgerServices.Com.au
WWW.KESTRELLEDGERSERVICES.COM.AU
Phone: +61 0488 517 934
23460 Marlow Valley Road Fernside QLD 4367, Australia

hi, I have uploaded an .EPS logo as requested by one of the designers, let me know if this is not the right size for the business card. thanks Jordan

Target Market(s)

Mainly Business clients

Industry/Entity Type

Business

Font styles to use
Serif

Colors
85acd3
3377b5

Requirements
Must have
• clean/crisp/well laid out

```html
<!DOCTYPE html>
<html lang="en">
<head>
<meta charset="utf-8">
<title>Kestrel Ledger Services – Business Card</title>
<link href="https://fonts.googleapis.com/css2?family=Open+Sans:ital,wght@0,400;0,600;0,700;1,400&family=PT+Serif:ital,wght@1,400;1,700&display=swap" rel="stylesheet">
<style>
  :root {
    --ink: #111111;
    --grey: #8c8c8c;
    --steel-blue: #6593b6;
    --text-blue: #5f8db3;
    --paper: #ffffff;
    --ring: #1a1a1a;
  }
  * { margin: 0; padding: 0; box-sizing: border-box; }
  html, body { width: 1200px; height: 750px; overflow: hidden; background: var(--paper); }
  .card {
    position: relative;
    width: 1200px;
    height: 750px;
    background: var(--paper);
    font-family: "Open Sans", Arial, sans-serif;
    color: var(--ink);
  }

  /* Brand block */
  .brand { position: absolute; left: 45px; top: 70px; width: 650px; }
  .brand-mark {
    position: absolute; left: 0; top: 4px;
    width: 150px; height: 150px; border-radius: 50%;
    background: var(--steel-blue);
  }
  .brand-name {
    position: absolute; left: 172px; top: -14px;
    font-size: 100px; font-weight: 400; letter-spacing: 2px;
    color: var(--ink); line-height: 1.2; white-space: nowrap;
  }
  .brand-entity {
    position: absolute; left: 178px; top: 130px;
    font-size: 28px; color: var(--grey); white-space: nowrap; letter-spacing: 0.5px;
  }
  .brand-credential {
    position: absolute; right: 0; top: 168px;
    font-family: "PT Serif", Georgia, serif; font-style: italic;
    font-size: 35px; color: var(--text-blue); white-space: nowrap;
  }

  /* Contact block */
  .contact { position: absolute; left: 48px; top: 326px; }
  .contact-phone {
    display: flex; align-items: center; gap: 16px;
    font-size: 40px; font-weight: 700; line-height: 1.1;
  }
  .contact-phone svg { width: 44px; height: 30px; }
  .contact-line { font-size: 30px; line-height: 46px; }
  .contact-phone + .contact-line { margin-top: 6px; }

  .divider-vertical {
    position: absolute; left: 736px; top: 75px;
    width: 3px; height: 386px; background: var(--steel-blue);
  }

  /* Person & address */
  .person { position: absolute; left: 770px; top: 162px; }
  .person-name { font-size: 42px; font-style: italic; white-space: nowrap; }
  .person-quals { font-size: 21px; font-style: normal; margin-left: 16px; }
  .person-role { font-size: 33px; font-weight: 700; color: var(--grey); line-height: 1.1; margin-top: -4px; }

  .address { position: absolute; left: 770px; top: 300px; }
  .address-abn { font-size: 22px; line-height: 30px; }
  .address-line { font-size: 32px; line-height: 46px; }
  .address-abn + .address-line { margin-top: 6px; }

  .divider-horizontal {
    position: absolute; left: 40px; top: 503px;
    width: 1120px; height: 3px; background: var(--steel-blue);
  }

  .tagline {
    position: absolute; left: 0; top: 522px; width: 1200px; text-align: center;
    font-family: "PT Serif", Georgia, serif; font-style: italic; font-weight: 700;
    font-size: 48px; color: var(--text-blue); letter-spacing: 0.5px;
  }

  /* Services band */
  .services {
    position: absolute; left: 0; top: 609px; width: 1200px; height: 141px;
    background: var(--steel-blue);
    display: flex; flex-direction: column; justify-content: center; align-items: center;
    gap: 6px;
  }
  .services-row {
    display: flex; align-items: center; gap: 14px;
    color: var(--paper); font-weight: 700; font-size: 33px; letter-spacing: 2.6px;
    white-space: nowrap; line-height: 42px;
  }
  .services-dot {
    width: 22px; height: 22px; border-radius: 50%;
    border: 4px solid var(--ring); flex: none;
  }
</style>
</head>
<body>
<div class="card">

  <div class="brand">
    <div class="brand-mark"></div>
    <div class="brand-name">KESTREL</div>
    <div class="brand-entity">LEDGER SERVICES PTY LTD</div>
    <div class="brand-credential">Registered Tax Agent</div>
  </div>

  <div class="contact">
    <div class="contact-phone">
      <svg viewBox="0 0 44 30" aria-hidden="true">
        <path d="M2 10 Q22 -2 42 10 L40 15 L32 13 L31 8 Q22 5 13 8 L12 13 L4 15 Z" fill="#5f8db3"/>
        <path d="M10 14 L34 14 L40 28 L4 28 Z" fill="#5f8db3"/>
        <circle cx="22" cy="21" r="4.5" fill="#ffffff"/>
      </svg>
      <span>+61 0488 517 934</span>
    </div>
    <div class="contact-line">jordan@kestrelledgerservices.com.au</div>
    <div class="contact-line">www.kestrelledgerservices.com.au</div>
  </div>

  <div class="divider-vertical"></div>

  <div class="person">
    <div class="person-name">Jordan Pike<span class="person-quals">B.Com CPA</span></div>
    <div class="person-role">DIRECTOR</div>
  </div>

  <div class="address">
    <div class="address-abn">ABN 47 382 615 908</div>
    <div class="address-line">23460 Marlow Valley Road</div>
    <div class="address-line">Fernside QLD 4367,</div>
    <div class="address-line">Australia</div>
  </div>

  <div class="divider-horizontal"></div>

  <div class="tagline">Professional advice tailored to suit you</div>

  <div class="services">
    <div class="services-row">
      <span>SUPERANNUATION</span><span class="services-dot"></span>
      <span>BUSINESS SERVICES</span><span class="services-dot"></span>
      <span>TAXATION</span>
    </div>
    <div class="services-row">
      <span>MANAGEMENT CONSULTING</span><span class="services-dot"></span>
      <span>SOFTWARE SUPPORT</span>
    </div>
  </div>

</div>
</body>
</html>
```